Crestline Gas and Plumbing Business Card Design

I am after a business card design for my plumbing business called 'Crestline Gas & Plumbing'. I do all types of plumbing and gas work and specialise in general maintenance plumbing. Would like to see designs using current logo

Industry/Entity Type

Plumbing

Contact Information for Business Card

Name - Dale Whitcombe
Phone number - 0455163027
Email - admin@crestlinegasandplumbing.example.com.au
ABN - 68204915336

```html
<!DOCTYPE html>
<html lang="en">
<head>
<meta charset="utf-8">
<title>Crestline Gas &amp; Plumbing — Business Card</title>
<link rel="stylesheet" href="https://fonts.googleapis.com/css2?family=Saira:wght@700&family=Lato:wght@400&display=swap">
<style>
  :root {
    --stage: #2b2b2b;
    --card: #121212;
    --card-edge: #1b1b1b;
    --brand-blue: #1f6fc4;
    --accent-orange: #f7a21b;
    --accent-orange-deep: #f08a12;
    --text-light: #d4d4d4;
    --rule: #5a5a5a;
  }
  * { box-sizing: border-box; margin: 0; padding: 0; }
  html, body {
    width: 1200px;
    height: 900px;
    overflow: hidden;
    background: var(--stage);
  }
  .stage {
    width: 1200px;
    height: 900px;
    display: flex;
    flex-direction: column;
    align-items: center;
    justify-content: center;
    gap: 40px;
  }
  .card {
    position: relative;
    width: 600px;
    height: 340px;
    background: linear-gradient(160deg, var(--card-edge), var(--card));
    overflow: hidden;
  }
  .card__band {
    position: absolute;
    left: 0;
    right: 0;
    bottom: 0;
    height: 10px;
    background: linear-gradient(90deg, var(--accent-orange), var(--accent-orange-deep));
  }

  /* Front */
  .card--front {
    display: flex;
    align-items: center;
    justify-content: center;
  }
  .brand {
    display: flex;
    align-items: center;
    gap: 16px;
    margin-bottom: 10px;
  }
  .brand__dot {
    width: 26px;
    height: 26px;
    border-radius: 50%;
    background: var(--accent-orange);
    flex: none;
  }
  .brand__name {
    font-family: "Saira", sans-serif;
    font-weight: 700;
    font-size: 30px;
    letter-spacing: 1px;
    text-transform: uppercase;
    color: var(--brand-blue);
  }

  /* Back */
  .card--back {
    display: flex;
    flex-direction: column;
    align-items: center;
    justify-content: center;
    padding-bottom: 14px;
    text-align: center;
  }
  .contact__name {
    font-family: "Saira", sans-serif;
    font-weight: 700;
    font-size: 26px;
    letter-spacing: 1.5px;
    text-transform: uppercase;
    color: var(--brand-blue);
  }
  .contact__rule {
    width: 170px;
    height: 1px;
    background: var(--rule);
    margin: 8px 0;
  }
  .contact__line {
    font-family: "Lato", sans-serif;
    font-weight: 400;
    font-size: 19px;
    color: var(--text-light);
    line-height: 1.3;
  }
  .contact__label { color: var(--accent-orange); }
</style>
</head>
<body>
  <main class="stage">
    <section class="card card--front" aria-label="Card front">
      <div class="brand">
        <span class="brand__dot" aria-hidden="true"></span>
        <span class="brand__name">Crestline Gas &amp; Plumbing</span>
      </div>
      <div class="card__band"></div>
    </section>

    <section class="card card--back" aria-label="Card back">
      <h1 class="contact__name">Dale Whitcombe</h1>
      <div class="contact__rule"></div>
      <p class="contact__line">0455163027</p>
      <p class="contact__line">admin@crestlinegasandplumbing.example.com.au</p>
      <div class="contact__rule"></div>
      <p class="contact__line"><span class="contact__label">ABN</span> - 68204915336</p>
      <div class="card__band"></div>
    </section>
  </main>
</body>
</html>
```